Fern Hollow Canine business card

I need a business card design for a dog training company in Toronto called Fern Hollow Canine. My training is unique, outdoor training that helps people create a better bond with their dog through communication and understanding their dog's true nature. I do not use treats - but communication and praise for the dog.

I help people create a better life for them and their dog. From puppy training right through to seniors, I offer both group classes called Curbside Calm Course as well as in-home private sessions.

I believe that having a dog is a lifestyle, so I encourage clients to incorporate their dog into their active life. Outdoor activities such as hiking, mental stimulation, proper care and healthy food for their dog are all keys to a healthy and happy dog.

I would like a fresh and modern look that works with my logo. I would like to convey fun, confidence and happiness.

My services are premium services. I am a Certified Dog Trainer, and offer value for money, but my prices are higher than other trainers.
Updates

Thank you to everyone who submitted designs! I'm so impressed with the level of creativity and the options that you all have given me. It will be a difficult choice for sure. As this was my first experience with Pixel Bazaar - it has been a great one.

marla.

Industry/Entity Type

Communication

Requirements
Must have
• Marla Quinby, CTE
Certified Trainer Educator
marla@fernhollowk9.ca
416-555-0178
fernhollowk9.ca

Prefer a double sided card.
Must have Fern Hollow Canine logo. File attached. I do have a stroke logo for a dark background as well.

Must only use the fonts and colours as outlined in my brand guidelines, which are attached.
Should not have
• no cheesy pet images
do not use the tongue as an element outside of the logo
minimize the use of pink - can be used as an accent colour but should not be a main colour

```html
<!DOCTYPE html>
<html lang="en">
<head>
<meta charset="utf-8">
<title>Fern Hollow Canine business cards</title>
<link rel="stylesheet" href="https://fonts.googleapis.com/css2?family=Source+Sans+3:wght@400;700;800&display=swap">
<style>
  :root {
    --backdrop: #9c6a47;
    --sky-light: #55c8f0;
    --sky-mid: #3fb0e2;
    --sky-edge: #2f95cc;
    --accent-pink: #f174ab;
    --divider: #2a5670;
    --charcoal: #3c3c3f;
    --ink-black: #000000;
    --paper-white: #ffffff;
    --grass-green: #8bb144;
  }
  * { box-sizing: border-box; margin: 0; padding: 0; }
  html, body {
    width: 1200px;
    height: 765px;
    overflow: hidden;
  }
  body {
    position: relative;
    background: var(--backdrop);
    font-family: "Source Sans 3", "Myriad Pro", Arial, sans-serif;
  }
  .card {
    position: absolute;
    width: 524px;
    height: 300px;
    border-radius: 12px;
    overflow: hidden;
  }
  .card--front { left: 52px; top: 66px; }
  .card--back-blue {
    left: 621px; top: 66px;
    background: radial-gradient(ellipse at 50% 40%, var(--sky-light) 0%, var(--sky-mid) 55%, var(--sky-edge) 100%);
  }
  .card--back-dark {
    left: 340px; top: 406px;
    background: var(--ink-black);
  }

  .front-brand-panel {
    position: absolute;
    left: 0; top: 0;
    width: 284px; height: 300px;
    background: radial-gradient(ellipse at 85% 50%, var(--sky-light) 0%, var(--sky-mid) 60%, var(--sky-edge) 100%);
  }
  .front-divider {
    position: absolute;
    left: 284px; top: 0;
    width: 3px; height: 300px;
    background: var(--divider);
  }
  .front-info-panel {
    position: absolute;
    left: 287px; top: 0;
    width: 237px; height: 300px;
    background: var(--accent-pink);
    color: var(--paper-white);
    padding: 98px 0 0 19px;
    font-size: 13px;
    line-height: 16px;
  }
  .contact-list {
    list-style: none;
    margin-top: 27px;
  }
  .contact-list li {
    display: flex;
    align-items: center;
    gap: 5px;
    height: 21px;
  }
  .contact-icon { width: 10px; height: 10px; flex: none; }

  .brand-wordmark {
    position: absolute;
    display: flex;
    align-items: center;
    gap: 10px;
    font-weight: 800;
    line-height: 0.95;
    letter-spacing: -0.5px;
  }
  .brand-dot { flex: none; border-radius: 50%; }
  .brand-wordmark--front {
    left: 26px; top: 98px;
    font-size: 40px;
    color: var(--charcoal);
  }
  .brand-wordmark--front .brand-dot { width: 18px; height: 18px; background: var(--charcoal); }
  .brand-wordmark--blue {
    left: 112px; top: 68px;
    font-size: 46px;
    color: var(--charcoal);
  }
  .brand-wordmark--blue .brand-dot { width: 22px; height: 22px; background: var(--charcoal); }
  .brand-wordmark--dark {
    left: 112px; top: 68px;
    font-size: 46px;
    color: var(--paper-white);
  }
  .brand-wordmark--dark .brand-dot { width: 22px; height: 22px; background: var(--paper-white); }

  .card-url {
    position: absolute;
    left: 0; right: 0;
    top: 257px;
    text-align: center;
    font-size: 13px;
    letter-spacing: 2.6px;
  }
  .card--back-blue .card-url { color: var(--ink-black); }
  .card--back-dark .card-url { color: var(--paper-white); }
</style>
</head>
<body>

  <section class="card card--front" aria-label="Business card front">
    <div class="front-brand-panel">
      <div class="brand-wordmark brand-wordmark--front">
        <span class="brand-dot"></span>
        <span>Fern<br>Hollow<br>Canine</span>
      </div>
    </div>
    <div class="front-divider"></div>
    <div class="front-info-panel">
      <p class="holder-name">Marla Quinby, CTE</p>
      <p class="holder-title">Certified Trainer Educator</p>
      <ul class="contact-list">
        <li>
          <svg class="contact-icon" viewBox="0 0 10 10" aria-hidden="true">
            <path d="M2.2 0.8 L3.6 2.6 L2.8 3.6 Q3.8 5.9 6.3 7.1 L7.3 6.3 L9.2 7.6 L8.4 9.2 Q3.6 9 0.8 2 Z" fill="none" stroke="#fff" stroke-width="1"/>
          </svg>
          <span>416-555-0178</span>
        </li>
        <li>
          <svg class="contact-icon" viewBox="0 0 10 10" aria-hidden="true">
            <rect x="1" y="2.5" width="8" height="5.5" fill="#fff"/>
            <path d="M1 2.5 L5 5.6 L9 2.5" fill="none" stroke="#f174ab" stroke-width="0.8"/>
          </svg>
          <span>marla@fernhollowk9.ca</span>
        </li>
        <li>
          <svg class="contact-icon" viewBox="0 0 10 10" aria-hidden="true">
            <circle cx="5" cy="5" r="4.2" fill="none" stroke="#fff" stroke-width="0.9"/>
            <ellipse cx="5" cy="5" rx="1.8" ry="4.2" fill="none" stroke="#fff" stroke-width="0.8"/>
            <line x1="0.8" y1="5" x2="9.2" y2="5" stroke="#fff" stroke-width="0.8"/>
          </svg>
          <span>www.fernhollowk9.ca</span>
        </li>
      </ul>
    </div>
  </section>

  <section class="card card--back-blue" aria-label="Business card back, blue">
    <div class="brand-wordmark brand-wordmark--blue">
      <span class="brand-dot"></span>
      <span>Fern<br>Hollow<br>Canine</span>
    </div>
    <p class="card-url">www.fernhollowk9.ca</p>
  </section>

  <section class="card card--back-dark" aria-label="Business card back, black">
    <div class="brand-wordmark brand-wordmark--dark">
      <span class="brand-dot"></span>
      <span>Fern<br>Hollow<br>Canine</span>
    </div>
    <p class="card-url">www.fernhollowk9.ca</p>
  </section>

</body>
</html>
```